Broadcaster,Conference Host,Facilitator

Looking for a business card and logo to create the Grant Felber brand .. Something with a slant towards radio and conference speaking
I like the idea of classic black white or grey but open to suggestions

Target Market(s)

Corporates

Industry/Entity Type

Business

Contact Information for Business Card

Grant Felber
Email : Grant.Felber@quorvamail.co.uk
Mobile : +44 7700 382046
Twitter : @Grantfelber

Font styles to use
Serif
Decorative
Script

Requirements
Must have
• Feel classy and dynamic
Should not have
• Cartoons

```html
<!DOCTYPE html>
<html lang="en">
<head>
<meta charset="utf-8">
<title>Grant Felber — Business Card</title>
<link href="https://fonts.googleapis.com/css2?family=Source+Sans+3:wght@400;600&family=Questrial&display=swap" rel="stylesheet">
<style>
  :root {
    --page-bg: #e9e6e2;
    --kraft-light: #cfae84;
    --kraft-mid: #c19f74;
    --kraft-dark: #b08c63;
    --ink: #111111;
    --rule: #3a2f22;
  }
  * { box-sizing: border-box; margin: 0; padding: 0; }
  html, body {
    width: 1200px;
    height: 900px;
    overflow: hidden;
  }
  body {
    position: relative;
    background: var(--page-bg);
    color: var(--ink);
  }
  .card {
    position: absolute;
    width: 556px;
    height: 342px;
    background: linear-gradient(135deg, var(--kraft-light) 0%, var(--kraft-mid) 55%, var(--kraft-dark) 100%);
    box-shadow: 0 6px 18px rgba(0, 0, 0, 0.18);
  }
  .card--contact { left: 238px; top: 62px; }
  .card--brand { left: 458px; top: 518px; width: 560px; }

  .contact {
    position: absolute;
    left: 0;
    right: 0;
    top: 116px;
    text-align: center;
    font-family: "Source Sans 3", sans-serif;
  }
  .contact__name {
    font-weight: 600;
    font-size: 21px;
    line-height: 1;
  }
  .contact__rule {
    width: 114px;
    height: 1px;
    margin: 15px auto 16px;
    background: var(--rule);
  }
  .contact__details {
    list-style: none;
    font-size: 16px;
    line-height: 22px;
  }

  .brand {
    position: absolute;
    left: 0;
    right: 0;
    top: 86px;
    text-align: center;
    font-family: "Questrial", sans-serif;
    font-weight: 400;
  }
  .brand__mark {
    display: block;
    font-size: 84px;
    line-height: 1;
    letter-spacing: 2px;
  }
  .brand__name {
    display: block;
    margin-top: 14px;
    font-size: 42px;
    line-height: 1;
  }
</style>
</head>
<body>
  <section class="card card--contact">
    <div class="contact">
      <h1 class="contact__name">Grant Felber</h1>
      <div class="contact__rule"></div>
      <ul class="contact__details">
        <li>+44 7700 382046</li>
        <li>Grant.Felber@quorvamail.co.uk</li>
        <li>@Grantfelber</li>
      </ul>
    </div>
  </section>

  <section class="card card--brand">
    <div class="brand">
      <span class="brand__mark">GF</span>
      <span class="brand__name">Grant Felber</span>
    </div>
  </section>
</body>
</html>
```